Package design for small honey and vegetable farm

I would like to have a unique design for the packaging of our honey and vegetables. I have attached the logo from our farm "Willow Creek Acres" that should be on the packaging for both the honey and the vegetables

For the honey the writing, "100% pure organic honey" must be on the packaging in some place. As well as "from the busy bees at Willow Creek Acres". I have attached some designs that I like.

For the vegetables. The design will need to go on a box like the one in the attached image. The phrase "Organically Grown" should be on the package. I would like the background color of the package to be black. I think I would also like to see some stylized vegetables (tomatoes in particular) on the package.

I would like to be able to get all the colors (RGB) used in the designs so I can pass them on to printers.

Industry/Entity Type

Farm

Colors
fbee3e

Requirements
Must have
• For the honey, the package it must say "100% pure organic honey".
• For the vegetables I would like the background color to be black. I would also like some stylized vegetables (tomatoes in particular) added to the package.

```html
<!DOCTYPE html>
<html lang="en">
<head>
<meta charset="utf-8">
<title>Willow Creek Acres – Organic Honey Label</title>
<link rel="stylesheet" href="https://fonts.googleapis.com/css2?family=Fenix&family=Caveat:wght@500&display=swap">
<style>
  :root {
    --backdrop: #e4e4e2;
    --label-paper: #f4f3ef;
    --honey-band: #d8a72a;
    --honey-drip: #dcae34;
    --gold-ink: #a07f1e;
    --gold-soft: #efe3bd;
    --script-ink: #2b2412;
  }
  html, body {
    margin: 0;
    width: 1200px;
    height: 800px;
    overflow: hidden;
    background: var(--backdrop);
  }
  .label-canvas { display: block; width: 1200px; height: 800px; }
  .label-paper { fill: var(--label-paper); }
  .honey-band { fill: var(--honey-band); }
  .honey-drip { fill: var(--honey-drip); }
  .quantity-tab { fill: var(--label-paper); }
  .bee-decoration { fill: var(--gold-soft); }
  .brand-name {
    font-family: "Fenix", Georgia, serif;
    font-size: 32px;
    fill: var(--gold-ink);
  }
  .claim-line {
    font-family: "Fenix", Georgia, serif;
    fill: var(--gold-ink);
  }
  .claim-pure { font-size: 44px; }
  .claim-organic { font-size: 74px; }
  .claim-honey { font-size: 48px; }
  .claim-frame {
    fill: none;
    stroke: var(--gold-ink);
    stroke-width: 1.6;
    stroke-dasharray: 4 4;
  }
  .tagline {
    font-family: "Caveat", cursive;
    font-weight: 500;
    font-size: 28px;
    fill: var(--script-ink);
  }
  .quantity-text {
    font-family: "Fenix", Georgia, serif;
    font-size: 16px;
    fill: var(--gold-ink);
  }
</style>
</head>
<body>
<svg class="label-canvas" viewBox="0 0 1200 800" xmlns="http://www.w3.org/2000/svg">
  <!-- Label body -->
  <rect class="label-paper" x="210" y="114" width="780" height="572"/>
  <rect class="honey-band" x="210" y="114" width="780" height="28"/>
  <rect class="honey-band" x="210" y="652" width="780" height="34"/>

  <!-- Faint large bee decoration -->
  <ellipse class="bee-decoration" role="img" aria-label="Faint line drawing of a large bee" cx="365" cy="390" rx="58" ry="80" opacity="0.6"/>

  <!-- Brand name -->
  <text class="brand-name" x="587" y="240" text-anchor="middle">Willow Creek Acres</text>

  <!-- Claim -->
  <rect class="claim-frame" x="457" y="306" width="278" height="80"/>
  <text class="claim-line claim-pure" x="596" y="366" text-anchor="middle">100% pure</text>

  <rect class="claim-frame" x="444" y="386" width="288" height="88"/>
  <text class="claim-line claim-organic" x="588" y="452" text-anchor="middle">organic</text>

  <rect class="claim-frame" x="444" y="482" width="248" height="68"/>
  <text class="claim-line claim-honey" x="568" y="532" text-anchor="middle">honey</text>

  <!-- Small bee -->
  <rect class="bee-decoration" role="img" aria-label="Small line drawing of a bee" x="372" y="490" width="58" height="56" rx="22"/>

  <!-- Honey drip -->
  <rect class="honey-drip" x="744" y="140" width="8" height="330"/>
  <path class="honey-drip" d="M744 465 C744 500 709 528 709 556 A39 39 0 0 0 787 556 C787 528 752 500 752 465 Z"/>

  <!-- Tagline -->
  <text class="tagline" x="567" y="594" text-anchor="middle">from the busy bees at</text>
  <text class="tagline" x="567" y="626" text-anchor="middle">Willow Creek Acres</text>

  <!-- Quantity tab -->
  <path class="quantity-tab" d="M520 686 C528 664 540 658 560 658 L614 658 C634 658 646 664 654 686 Z"/>
  <text class="quantity-text" x="587" y="679" text-anchor="middle">Quantity</text>
</svg>
</body>
</html>
```